Business Card for a mobile physiotherapy company

I need a layout for a business card for a mobile physiotherapy company.
Slogan is "Mobile Physiotherapy - Your Road To Recovery"
Phone number is 867-412-5093
Email VantePhysio@mailbox-demo.ca (subject to change with website)
Website www.VantePhysio.ca
My name and credentials: Gil Varney Gil Varney, BSc(kin), MPT, CAFCI, IMS
Information maybe included: Direct Billing, Services including Physiotherapy, IMS, acupuncture
Maybe include facebook and instagram logos
One side with the logo clean and sharp
Other side with details, try not to look too busy, keep everything concise

```html
<!DOCTYPE html>
<html lang="en">
<head>
<meta charset="utf-8">
<title>Vante Physio – Business Card</title>
<link href="https://fonts.googleapis.com/css2?family=Mulish:wght@400;700;800&display=swap" rel="stylesheet">
<style>
  :root {
    --navy: #284169;
    --green: #0c4a3c;
    --card-light: #e6e6e6;
    --grey-text: #6f6f6f;
    --white: #ffffff;
    --page: #e2e2e2;
  }
  * { box-sizing: border-box; margin: 0; padding: 0; }
  html, body {
    width: 1200px; height: 1200px; overflow: hidden;
    background: var(--page);
    font-family: "Mulish", sans-serif;
  }
  .card {
    position: absolute; left: 227px; width: 746px; height: 425px;
  }
  .card--front { top: 135px; background: var(--card-light); }
  .card--back  { top: 640px; background: var(--navy); }

  .brand {
    font-weight: 800; color: var(--navy); letter-spacing: 1px;
    white-space: nowrap;
  }
  .card--front .brand {
    position: absolute; left: 37px; top: 120px; font-size: 40px;
  }
  .person-name {
    position: absolute; left: 33px; top: 228px;
    font-size: 23px; font-weight: 700; color: var(--navy);
  }
  .credentials {
    position: absolute; left: 33px; top: 262px;
    font-size: 16px; color: var(--grey-text);
  }
  .contacts {
    position: absolute; left: 33px; top: 299px; list-style: none;
  }
  .contacts li {
    display: flex; align-items: center; gap: 9px;
    height: 24px; font-size: 17px; color: var(--grey-text);
  }
  .contacts svg { width: 19px; height: 19px; flex: none; }

  .rule {
    position: absolute; left: 0; right: 0; top: 382px; height: 3px;
    background: var(--green);
  }
  .services-band {
    position: absolute; left: 0; right: 0; top: 389px; bottom: 0;
    background: var(--navy); color: var(--white);
    font-size: 16.5px; padding-left: 34px;
    display: flex; align-items: center;
  }

  .card--back .brand {
    position: absolute; left: 0; right: 0; top: 150px;
    text-align: center; color: var(--white); font-size: 54px;
  }
  .slogan {
    position: absolute; left: 0; right: 0; top: 298px;
    text-align: center; color: var(--white); font-size: 17.5px;
  }
  .social {
    position: absolute; top: 361px; left: 342px;
    display: flex; gap: 6px;
  }
  .social span {
    width: 28px; height: 28px; border-radius: 50%; background: var(--white);
  }
</style>
</head>
<body>
  <section class="card card--front">
    <div class="brand">Vante Physio</div>
    <h1 class="person-name">Gil Varney Gil Varney</h1>
    <p class="credentials">BSc(kin), MPT, CAFCI, IMS</p>
    <ul class="contacts">
      <li>
        <svg viewBox="0 0 20 20"><circle cx="10" cy="10" r="10" fill="#284169"/><path d="M6.5 5.5l2 .2.8 2.3-1.2.9a6 6 0 0 0 3 3l.9-1.2 2.3.8.2 2c-.5.9-1.5 1.2-2.5 1A9 9 0 0 1 5.5 8c-.2-1 .1-2 1-2.5z" fill="#fff"/></svg>
        867-412-5093
      </li>
      <li>
        <svg viewBox="0 0 20 20"><circle cx="10" cy="10" r="10" fill="#284169"/><rect x="5" y="6.5" width="10" height="7" fill="none" stroke="#fff" stroke-width="1.1"/><path d="M5 6.5l5 4 5-4" fill="none" stroke="#fff" stroke-width="1.1"/></svg>
        VantePhysio@mailbox-demo.ca
      </li>
      <li>
        <svg viewBox="0 0 20 20"><circle cx="10" cy="10" r="10" fill="#284169"/><g fill="none" stroke="#fff" stroke-width="1"><circle cx="10" cy="10" r="5.5"/><ellipse cx="10" cy="10" rx="2.4" ry="5.5"/><path d="M4.5 10h11M5.5 7.3h9M5.5 12.7h9"/></g></svg>
        www.VantePhysio.ca
      </li>
    </ul>
    <div class="rule"></div>
    <p class="services-band">Direct Billing, Services including Physiotherapy, IMS, acupuncture</p>
  </section>

  <section class="card card--back">
    <div class="brand">Vante Physio</div>
    <p class="slogan">Mobile Physiotherapy - Your Road To Recovery</p>
    <div class="social" aria-label="Social media links">
      <span></span><span></span>
    </div>
  </section>
</body>
</html>
```